Design AND code an HTML landing page

A landing page for campaigns and webinars respondents for project www.brevamor-homes.example. We expect the design to be coded. We will provide the copy and content. It will be a simple landing page for a new development project, to capture details of any potential clients showing interest, including any leads generated via webinars.

Broad instructions are as follows:
- It should not have a header or footer. Minimum escape links as possible.
- Create a lead generator box to get e-mails / relevant info of people interested.
- If possible, add a virtual tour (link to host server provided) at the top of the page.
- Content will be provided
- An option to include a link to a ClipVerra video

Target Market(s)

Pre/retiree and retirees

Industry/Entity Type

Real estate development, retirement, relocation, travel and tourism

Coding

Coded - Design and coding required

Font styles to use
Other font styles liked:
• Preferably same as existing site

Colors
FFF300
FFF600
FEFA6F
FFFEC7
FFFEE8

Requirements
Must have
• Simple yet appealing look and feel, within the motif of the project, simple list of questions
Should not have
• Emojis, unrelated graphics, excessive graphics that are not linked to project

```html
<!DOCTYPE html>
<html lang="en">
<head>
<meta charset="utf-8">
<title>Brevamor Homes – Discover Most Suitable Property</title>
<link href="https://fonts.googleapis.com/css2?family=Urbanist:wght@300;400;500;600;700;800&display=swap" rel="stylesheet">
<style>
:root{
  --yellow:#e3cb34;
  --yellow-bright:#ffe000;
  --yellow-pale:#f6eec0;
  --ink:#23231a;
  --ink-soft:#4a4a3c;
  --muted:#9a9a90;
  --line:#d9d9d2;
  --gray-bg:#f5f5f5;
  --beige:#faf1e8;
  --brown:#8a6a3a;
  --white:#ffffff;
}
*{box-sizing:border-box;margin:0;padding:0}
html,body{width:1200px;height:3839px;overflow:hidden}
body{font-family:"Urbanist",sans-serif;color:var(--ink);background:var(--white);position:relative}
.abs{position:absolute}

/* Hero */
.hero{left:0;top:0;width:1200px;height:698px;overflow:hidden;
  background:linear-gradient(180deg,#8fc3ec 0%,#cfe5f6 38%,#b9b6a0 62%,#3e3a30 82%,#2a2620 100%)}
.hero-photo{position:absolute;left:380px;top:140px;width:820px;height:558px;
  background:linear-gradient(160deg,#55524a 0%,#2b2924 45%,#1f1d19 100%);
  clip-path:polygon(0 62%,100% 0,100% 100%,0 100%)}
.hero-pool{position:absolute;left:0;top:590px;width:520px;height:108px;
  background:linear-gradient(180deg,#6d8f6a 0%,#4ea1c9 45%,#3a4a34 100%)}
.hero-halo{left:18px;top:142px;width:250px;height:250px;border-radius:50%;background:rgba(255,255,255,.35)}
.wordmark{font-size:36px;font-weight:500;color:var(--ink-soft);line-height:1;white-space:nowrap}
.hero-brand{left:389px;top:50px;width:190px;text-align:center}
.hero-divider{left:603px;top:40px;width:1px;height:62px;background:rgba(255,255,255,.6)}
.btn-tour{left:653px;top:47px;width:170px;height:43px;border-radius:22px;background:#1f2430;color:#fff;
  font-size:17px;font-weight:500;display:flex;align-items:center;justify-content:center;gap:12px;text-decoration:none}
.hero-title{left:100px;top:172px;font-size:64px;font-weight:800;line-height:66px;color:#1c1c18;letter-spacing:-.5px}
.hero-sub{left:100px;top:392px;width:340px;font-size:17px;line-height:24px;color:#2a2a24}
.hero-notch{left:560px;top:682px}

/* About */
.about{left:0;top:698px;width:1200px;height:640px;background:var(--yellow)}
.about-title{left:127px;top:826px;font-size:38px;font-weight:700;line-height:44px;color:#2a2a12}
.about-rule{left:127px;top:882px;width:40px;height:3px;background:#b88f1b}
.about-text{left:127px;top:906px;width:420px;font-size:15.5px;line-height:29.5px;color:#2a2a12}
.about-img1{left:602px;top:793px;width:252px;height:337px;background:linear-gradient(160deg,#c59a6d,#4f5d3a 55%,#2c2f2a);box-shadow:0 10px 24px rgba(0,0,0,.3)}
.about-img2{left:872px;top:838px;width:188px;height:247px;background:linear-gradient(160deg,#d1b07a,#3e6fa8 55%,#6b7a6a);box-shadow:0 10px 24px rgba(0,0,0,.3)}
.wave{left:0;width:1200px}

/* Facilities */
.fac-line{left:599px;top:1258px;width:1px;height:96px;background:#c8c8c8}
.fac-dot{left:596px;top:1352px;width:7px;height:7px;border-radius:50%;background:#3b8ee0}
.section-title{width:1200px;left:0;text-align:center;font-weight:700}
.fac-title{top:1360px;font-size:38px}
.fac-title span{color:var(--yellow)}
.fac-sub{top:1415px;font-size:15px;color:#3a3a30}
.fac-card{top:1479px;width:231px;height:231px}
.fac-card.c1{left:234px;background:linear-gradient(150deg,#7f8b55,#2e3a2a 55%,#4fb3c9 80%,#35402e);clip-path:polygon(0 0,100% 0,100% 100%,0 96%)}
.fac-card.c2{left:484px;background:linear-gradient(180deg,#6f9fd0,#a9c6df 40%,#4a4e52 60%,#1f2125)}
.fac-card.c3{left:735px;background:linear-gradient(160deg,#5d9de0,#c6d7e6 35%,#6b6450 65%,#4e7a34);clip-path:polygon(0 4%,100% 0,100% 96%,0 100%)}
.fac-caption{left:484px;top:1652px;width:231px;text-align:center;color:#fff;font-size:14px}
.arrow-btn{top:1578px;width:28px;height:28px;border-radius:50%;background:#fff;box-shadow:0 2px 6px rgba(0,0,0,.15);display:flex;align-items:center;justify-content:center}

/* Reasons */
.reason-title{top:1836px;font-size:43px;line-height:46px}
.reason-title small{display:block;font-size:35px}
.reason-rule{left:580px;top:1946px;width:40px;height:3px;background:var(--brown)}
.feature{width:106px;height:106px;border-radius:50%;background:#fff;box-shadow:0 3px 10px rgba(0,0,0,.12);display:flex;align-items:center;justify-content:center}
.feature-label{width:160px;text-align:center;font-size:14px;font-weight:600;color:#4a4a40}
.hub-brand{left:0;top:2382px;width:1200px;text-align:center}

/* Contact form */
.touch{left:0;top:2612px;width:1200px;height:740px;background:var(--gray-bg)}
.touch-photo{left:236px;top:2712px;width:356px;height:295px;background:linear-gradient(135deg,#d6c24a,#b8a535 50%,#8f8330)}
.form-card{left:401px;top:2803px;width:570px;height:402px;background:#fff;box-shadow:0 8px 30px rgba(0,0,0,.06)}
.form-title{position:absolute;left:48px;top:40px;font-size:25px;font-weight:300;letter-spacing:.3px}
.form-title b{font-weight:700}
.field{position:absolute;width:208px;border-bottom:1px solid var(--line);padding-bottom:8px}
.field.wide{width:458px}
.field label{display:block;font-size:9px;font-weight:700;color:#333;text-transform:uppercase;margin-bottom:6px}
.field span{font-size:10px;color:var(--muted)}
.send{position:absolute;left:468px;top:303px;width:50px;height:50px;border-radius:50%;background:var(--yellow);display:flex;align-items:center;justify-content:center}

/* Contact us */
.contact{left:0;top:3240px;width:1200px;height:599px}
.contact-title{top:3420px;font-size:38px}
.contact-sub{top:3475px;font-size:15px;font-weight:500}
.icon-circle{top:3521px;width:120px;height:120px;border-radius:50%;background:#fff;display:flex;align-items:center;justify-content:center}
.contact-divider{left:600px;top:3540px;width:1px;height:210px;background:#b39e25}
.contact-col{width:400px;text-align:center}
.contact-col h3{font-size:24px;font-weight:700}
.contact-col p{font-size:21px;margin-top:16px}
</style>
</head>
<body>

<!-- Hero -->
<section class="abs hero" aria-label="Hero">
  <div class="hero-photo" role="img" aria-label="Modern apartment building with wooden balcony screens at dusk"></div>
  <div class="hero-pool" role="img" aria-label="Pool deck with white parasols and sun loungers"></div>
</section>
<div class="abs hero-halo"></div>
<div class="abs wordmark hero-brand">Brevamor</div>
<div class="abs hero-divider"></div>
<a class="abs btn-tour" href="#">Virtual Tour
  <svg width="10" height="12" viewBox="0 0 10 12"><path d="M0 0L10 6L0 12Z" fill="#fff"/></svg></a>
<h1 class="abs hero-title">Discover<br>Most Suitable<br>Property</h1>
<p class="abs hero-sub">Helping you to get your perfect properties in the world, with the fastest way.</p>

<!-- About -->
<section class="abs about" aria-label="About"></section>
<svg class="abs hero-notch" width="80" height="18" viewBox="0 0 80 18"><path d="M0 18Q20 18 40 0Q60 18 80 18Z" fill="var(--yellow)"/><path d="M34 6h12l-6 6z" fill="#f5d000"/></svg>
<h2 class="abs about-title">About Brevamor Homes</h2>
<div class="abs about-rule"></div>
<p class="abs about-text">Nestled in the lush jungle of Bali between Canggu and Ubud, our incredible property sits on 2.3 hectares of land with a large river that flows through. We host 10 rooms at present and soon to be 30 more, expanding our scenic space so we can co-create new ideas, projects and technology that enable a healthier lifestyle.</p>
<div class="abs about-img1" role="img" aria-label="Aerial view of the residence block among hillside houses"></div>
<div class="abs about-img2" role="img" aria-label="Rooftop view over the pool and parking court"></div>
<svg class="abs wave" style="top:1180px" width="1200" height="160" viewBox="0 0 1200 160">
  <path d="M0 20C120 60 200 120 360 130C560 145 700 60 880 55C1020 52 1120 90 1200 100V160H0Z" fill="var(--yellow-pale)"/>
  <path d="M0 50C140 110 260 140 420 130C600 118 720 60 900 70C1040 78 1130 110 1200 140V160H0Z" fill="#fff"/>
</svg>

<!-- Facilities -->
<div class="abs fac-line"></div>
<div class="abs fac-dot"></div>
<h2 class="abs section-title fac-title">The <span>Facilities</span></h2>
<p class="abs section-title fac-sub" style="font-weight:400">Lorem ipsum dolor sit amet, consectetur adipiscing elit. Nulla laoreet eros</p>
<div class="abs fac-card c1" role="img" aria-label="Aerial view of the terraced building and pool"></div>
<div class="abs fac-card c2" role="img" aria-label="Rooftop terrace with sea view"></div>
<div class="abs fac-card c3" role="img" aria-label="Building facade over a green lawn"></div>
<div class="abs fac-caption">Facilities<br>
  <svg width="30" height="12" viewBox="0 0 30 12"><path d="M3 9l4-4M5 3l2-2 3 3-2 2M2 8l-1 1 2 2 1-1" stroke="#fff" fill="none" stroke-width="1.2"/><ellipse cx="22" cy="6" rx="6" ry="3.5" stroke="#fff" fill="none" stroke-width="1.2"/><circle cx="22" cy="6" r="1.5" fill="#fff"/></svg></div>
<div class="abs arrow-btn" style="left:114px"><svg width="10" height="10" viewBox="0 0 10 10"><path d="M9 5H1M4 2L1 5l3 3" stroke="#555" fill="none" stroke-width="1.3"/></svg></div>
<div class="abs arrow-btn" style="left:1057px"><svg width="10" height="10" viewBox="0 0 10 10"><path d="M1 5h8M6 2l3 3-3 3" stroke="#3b8ee0" fill="none" stroke-width="1.3"/></svg></div>

<!-- Reasons -->
<h2 class="abs section-title reason-title">Its the worlds #1<small>Destination for a reason</small></h2>
<div class="abs reason-rule"></div>
<svg class="abs" style="left:0;top:1980px" width="1200" height="560" viewBox="0 1980 1200 560">
  <path d="M236 2390C240 2260 300 2200 322 2147C400 2070 500 2040 600 2035C700 2040 800 2070 872 2147C900 2200 960 2260 966 2390" fill="none" stroke="#d9cdb8" stroke-width="1.5" stroke-dasharray="5 5"/>
  <path d="M428 2465A175 175 0 1 1 772 2465" fill="none" stroke="#e6d9c6" stroke-width="1.5" stroke-dasharray="5 5"/>
  <circle cx="600" cy="2400" r="127" fill="var(--beige)"/>
  <circle cx="600" cy="2400" r="92" fill="#fff"/>
</svg>
<div class="abs wordmark hub-brand">Brevamor</div>

<div class="abs feature" style="left:547px;top:1982px"><svg width="66" height="56" viewBox="0 0 66 56" fill="#2e2a1e"><rect x="4" y="6" width="3" height="44"/><rect x="0" y="6" width="2" height="16"/><rect x="9" y="6" width="2" height="16"/><circle cx="33" cy="30" r="17" fill="none" stroke="#2e2a1e" stroke-width="4"/><circle cx="33" cy="30" r="10"/><path d="M58 6c6 4 6 16 0 20v24h-3V6z"/></svg></div>
<div class="abs feature-label" style="left:520px;top:2102px">The Feature</div>

<div class="abs feature" style="left:269px;top:2094px"><svg width="44" height="56" viewBox="0 0 44 56" fill="#2e2a1e"><path d="M8 2h28l8 10-22 20L0 12z"/><path d="M4 40h6v14H4zM12 42h14c6 0 10-4 14-6v4c-4 4-9 8-16 8H12z"/></svg></div>
<div class="abs feature-label" style="left:244px;top:2214px">The Feature</div>

<div class="abs feature" style="left:819px;top:2094px"><svg width="60" height="52" viewBox="0 0 60 52" fill="#2e2a1e"><path d="M20 30C14 16 26 2 50 0c0 22-12 34-30 30zM24 26c6-6 12-10 20-16"/><path d="M2 34c8-2 16 0 22 4h14c4 0 4 4 0 4H24v2h18l14-8c4-2 6 2 2 4L40 50H14L2 44z"/></svg></div>
<div class="abs feature-label" style="left:794px;top:2214px">The Feature</div>

<div class="abs feature" style="left:183px;top:2337px"><svg width="56" height="56" viewBox="0 0 56 56"><circle cx="28" cy="28" r="17" fill="none" stroke="#2e2a1e" stroke-width="9" stroke-dasharray="7 4.3"/><circle cx="28" cy="28" r="14" fill="#2e2a1e"/><circle cx="28" cy="28" r="6" fill="#fff"/></svg></div>
<div class="abs feature-label" style="left:158px;top:2456px">The Feature</div>

<div class="abs feature" style="left:913px;top:2337px"><svg width="40" height="60" viewBox="0 0 40 60" fill="#2e2a1e"><circle cx="22" cy="8" r="6"/><path d="M16 16h12l8-10 3 2-9 14v12l6 22h-6l-6-18-6 18h-6l4-24-10-14 3-2z"/></svg></div>
<div class="abs feature-label" style="left:888px;top:2456px">The Feature</div>

<!-- Get in touch -->
<section class="abs touch" aria-label="Get in touch"></section>
<div class="abs touch-photo" role="img" aria-label="Two colleagues working at a laptop, yellow toned"></div>
<form class="abs form-card">
  <h2 class="form-title">GET IN <b>TOUCH</b></h2>
  <div class="field" style="left:54px;top:100px"><label>First name *</label><span>Marlow</span></div>
  <div class="field" style="left:303px;top:100px"><label>Last name*</label><span>Fenwick</span></div>
  <div class="field" style="left:54px;top:161px"><label>Email address*</label><span>marlowfenwick@mail.example</span></div>
  <div class="field" style="left:303px;top:161px"><label>Phone*</label><span>555-014-2288</span></div>
  <div class="field wide" style="left:54px;top:222px"><label>Company name</label><span>Company Name</span></div>
  <div class="field wide" style="left:54px;top:283px;padding-bottom:24px"><label>Message</label><span>Hi, do you have a moment to talk abo...|</span></div>
  <div class="send"><svg width="20" height="20" viewBox="0 0 20 20"><path d="M18 2L2 9l6 2 2 6z" fill="#fff"/></svg></div>
</form>

<!-- Contact us -->
<svg class="abs contact" viewBox="0 0 1200 599" width="1200" height="599" preserveAspectRatio="none">
  <path d="M0 40C120 20 220 60 360 70C520 80 640 40 800 30C960 20 1080 40 1200 60V599H0Z" fill="var(--yellow-pale)"/>
  <path d="M0 80C150 50 260 90 420 100C600 110 720 60 880 50C1020 42 1120 70 1200 90V599H0Z" fill="var(--yellow)"/>
</svg>
<h2 class="abs section-title contact-title">Contact Us</h2>
<p class="abs section-title contact-sub">We are here to help You</p>
<div class="abs icon-circle" style="left:283px"><svg width="60" height="60" viewBox="0 0 60 60" fill="none" stroke="var(--yellow)" stroke-width="2"><path d="M12 8l8-2 6 12-5 4c3 8 9 14 17 17l4-5 12 6-2 8c-20 2-42-20-40-40z"/><path d="M34 10v4M40 8v4M46 12l-3 3M50 18h-4M34 20h4" stroke-dasharray="2 2"/></svg></div>
<div class="abs icon-circle" style="left:764px"><svg width="56" height="42" viewBox="0 0 56 42" fill="none" stroke="var(--yellow)" stroke-width="2"><rect x="2" y="2" width="52" height="38"/><path d="M2 2l26 22L54 2M2 40l20-20M54 40L34 20"/></svg></div>
<div class="abs contact-divider"></div>
<div class="abs contact-col" style="left:138px;top:3660px"><h3>Have questions? Call Us.</h3><p>+1 555 010 4471</p></div>
<div class="abs contact-col" style="left:625px;top:3660px"><h3>Email Us</h3><p>hello@brevamor-homes.example</p></div>

</body>
</html>
```